CEO Business card - hotels and restaurant

Business card for the General Manager of 3 different businesses: 2 hotels and 1 restaurant:
Quinta Serrana Hotel
Casa Ormonde - Miravel Hotel
pão com toda alegria restaurant
Name and contact details:
Rui Fontelas Marques
CEO
E-mail: rui.marques@quintaserranahotel.com
Mobile: +351 917 443 261
Please find the attached logos. You may also google it for the 3 businesses

Industry/Entity Type

Hospitality

Contact Information for Business Card

Rui Fontelas Marques
CEO

Font styles to use
Script

Colors

Designer to choose colors to be used in the design.

Requirements
Must have
• Front - Name, position and contact details
• Back - Businesses logos and info of each one
• HOTEL QUINTA SERRANA
• Address: Rua Padre Anselmo - Nº 173 | 2440-627 BATALHA - PORTUGAL
• Phone: +351 244 581 392
• E-mail: geral@quintaserranahotel.pt
• HOTEL CASA ORMONDE - MIRAVEL
• Address: Avenida dos Cedros, s/n | 7350-218 ELVAS - PORTUGAL
• Phone: +351 268 472 519
• E-mail: geral@hotelcormonde-miravel.pt
• "pão com toda alegria" RESTAURANT
• Address: Estrada do Pinhal, 42 | 2440-356 BATALHA - PORTUGAL
• Phone: +351 244 615 284
• E-mail: info@pcta.pt
Nice to have
• Something elegant and stylish but professional and very wow effect

```html
<!DOCTYPE html>
<html lang="pt">
<head>
<meta charset="utf-8">
<title>Rui Fontelas Marques – CEO Business Card</title>
<link rel="stylesheet" href="https://fonts.googleapis.com/css2?family=Cinzel:wght@400&family=Open+Sans:wght@400;700&display=swap">
<style>
  :root {
    --canvas: #d3d4d6;
    --ink-black: #141414;
    --wine: #4e1028;
    --wine-bright: #8c1a45;
    --paper: #ffffff;
    --text-grey: #555555;
    --divider: #9a9a9a;
    --icon-light: #ececec;
    --name-ivory: #ebe8e3;
  }
  * { margin: 0; padding: 0; box-sizing: border-box; }
  html, body { width: 1200px; height: 1000px; overflow: hidden; }
  body {
    background: var(--canvas);
    position: relative;
    font-family: "Open Sans", Arial, sans-serif;
  }
  .icon-defs { position: absolute; width: 0; height: 0; }

  /* Front */
  .card-front {
    position: absolute; left: 242px; top: 64px; width: 716px; height: 419px;
    background: var(--wine); overflow: hidden;
  }
  .front-header {
    position: absolute; left: 0; top: 0; width: 100%; height: 130px;
    background: var(--ink-black);
    border-bottom: 2px solid var(--paper);
  }
  .holder-name {
    position: absolute; left: 0; top: 64px; width: 100%;
    text-align: center; font-family: "Cinzel", Georgia, serif;
    font-weight: 400;
    font-size: 40px; line-height: 48px; color: var(--name-ivory);
    letter-spacing: 0;
  }
  .holder-role {
    position: absolute; left: 283px; top: 128px; width: 151px; height: 34px;
    background: var(--ink-black);
    border: 2px solid var(--paper); border-top: none;
    font-family: "Cinzel", Georgia, serif; font-size: 30px; line-height: 30px;
    font-weight: 400;
    color: var(--name-ivory); text-align: center; letter-spacing: 14px;
    padding-left: 14px;
  }
  .front-contact {
    position: absolute; left: 0; width: 100%; text-align: center;
    color: var(--paper); font-size: 16px;
  }
  .front-contact svg { display: block; margin: 0 auto 9px; width: 32px; height: 32px; }
  .front-contact.phone { top: 213px; }
  .front-contact.email { top: 306px; }

  /* Back */
  .card-back {
    position: absolute; left: 242px; top: 517px; width: 716px; height: 419px;
    background: var(--ink-black);
  }
  .venue {
    position: absolute; left: 0; width: 100%; height: 119px;
    background: var(--paper);
  }
  .venue + .venue { border-top: 1.5px solid var(--divider); }
  .venue:nth-of-type(1) { top: 30px; }
  .venue:nth-of-type(2) { top: 149px; }
  .venue:nth-of-type(3) { top: 269px; height: 119px; border-bottom: 1.5px solid var(--divider); }
  .venue-mark {
    position: absolute; left: 20px; top: 0; width: 196px; height: 100%;
    display: flex; align-items: center; justify-content: center; gap: 8px;
    font-weight: 700; font-size: 19px; color: var(--wine-bright); text-align: center;
    line-height: 1.15;
  }
  .venue-mark .dot { width: 12px; height: 12px; border-radius: 50%; background: var(--wine-bright); flex: none; }
  .venue-info { position: absolute; left: 226px; top: 12px; }
  .venue-title { font-weight: 700; font-size: 16px; color: var(--wine-bright); line-height: 22px; }
  .venue-line {
    display: flex; align-items: center; gap: 4px;
    font-size: 14px; color: var(--text-grey); line-height: 20px;
  }
  .venue-line svg { width: 17px; height: 17px; flex: none; }
</style>
</head>
<body>

<svg class="icon-defs" aria-hidden="true">
  <defs>
    <symbol id="icon-phone" viewBox="0 0 32 32">
      <path d="M11 21 L20 10" stroke="currentColor" stroke-width="2.6" stroke-linecap="round" fill="none"/>
      <rect x="18" y="7" width="5" height="5" rx="1.2" transform="rotate(45 20.5 9.5)" fill="currentColor"/>
      <rect x="9" y="19" width="5" height="5" rx="1.2" transform="rotate(45 11.5 21.5)" fill="currentColor"/>
    </symbol>
    <symbol id="icon-mail" viewBox="0 0 32 32">
      <rect x="8" y="10" width="16" height="12" rx="1.5" fill="currentColor"/>
      <path d="M8.5 11 L16 17 L23.5 11" stroke="var(--icon-stroke, #fff)" stroke-width="1.6" fill="none"/>
    </symbol>
    <symbol id="icon-pin" viewBox="0 0 32 32">
      <path d="M16 7 a7 7 0 0 1 7 7 c0 5 -7 11 -7 11 s-7 -6 -7 -11 a7 7 0 0 1 7 -7z" fill="none" stroke="currentColor" stroke-width="2.4"/>
      <circle cx="16" cy="14" r="2.4" fill="currentColor"/>
    </symbol>
  </defs>
</svg>

<section class="card-front">
  <div class="front-header"></div>
  <h1 class="holder-name">Rui Fontelas Marques</h1>
  <div class="holder-role">CEO</div>

  <div class="front-contact phone">
    <svg viewBox="0 0 32 32"><circle cx="16" cy="16" r="16" fill="var(--icon-light)"/><use href="#icon-phone" style="color: var(--wine)"/></svg>
    +351 917 443 261
  </div>
  <div class="front-contact email">
    <svg viewBox="0 0 32 32" style="--icon-stroke: var(--icon-light)"><circle cx="16" cy="16" r="16" fill="var(--icon-light)"/><use href="#icon-mail" style="color: var(--wine)"/></svg>
    rui.marques@quintaserranahotel.com
  </div>
</section>

<section class="card-back">
  <article class="venue">
    <div class="venue-mark">Quinta Serrana</div>
    <div class="venue-info">
      <h2 class="venue-title">HOTEL QUINTA SERRANA</h2>
      <p class="venue-line"><svg viewBox="0 0 32 32"><circle cx="16" cy="16" r="16" fill="var(--wine-bright)"/><use href="#icon-pin" style="color:#fff"/></svg>Rua Padre Anselmo - Nº 173 | 2440-627 BATALHA - PORTUGAL</p>
      <p class="venue-line"><svg viewBox="0 0 32 32"><circle cx="16" cy="16" r="16" fill="var(--wine-bright)"/><use href="#icon-phone" style="color:#fff"/></svg>+351 244 581 392</p>
      <p class="venue-line"><svg viewBox="0 0 32 32" style="--icon-stroke: var(--wine-bright)"><circle cx="16" cy="16" r="16" fill="var(--wine-bright)"/><use href="#icon-mail" style="color:#fff"/></svg>geral@quintaserranahotel.pt</p>
    </div>
  </article>

  <article class="venue">
    <div class="venue-mark">Casa Ormonde</div>
    <div class="venue-info">
      <h2 class="venue-title">HOTEL CASA ORMONDE - MIRAVEL</h2>
      <p class="venue-line"><svg viewBox="0 0 32 32"><circle cx="16" cy="16" r="16" fill="var(--wine-bright)"/><use href="#icon-pin" style="color:#fff"/></svg>Avenida dos Cedros, s/n | 7350-218 ELVAS - PORTUGAL</p>
      <p class="venue-line"><svg viewBox="0 0 32 32"><circle cx="16" cy="16" r="16" fill="var(--wine-bright)"/><use href="#icon-phone" style="color:#fff"/></svg>+351 268 472 519</p>
      <p class="venue-line"><svg viewBox="0 0 32 32" style="--icon-stroke: var(--wine-bright)"><circle cx="16" cy="16" r="16" fill="var(--wine-bright)"/><use href="#icon-mail" style="color:#fff"/></svg>geral@hotelcormonde-miravel.pt</p>
    </div>
  </article>

  <article class="venue">
    <div class="venue-mark"><span class="dot"></span>pão com<br>toda alegria</div>
    <div class="venue-info">
      <h2 class="venue-title">RESTAURANT "pão com toda alegria"</h2>
      <p class="venue-line"><svg viewBox="0 0 32 32"><circle cx="16" cy="16" r="16" fill="var(--wine-bright)"/><use href="#icon-pin" style="color:#fff"/></svg>Estrada do Pinhal, 42 | 2440-356 BATALHA - PORTUGAL</p>
      <p class="venue-line"><svg viewBox="0 0 32 32"><circle cx="16" cy="16" r="16" fill="var(--wine-bright)"/><use href="#icon-phone" style="color:#fff"/></svg>+351 244 615 284</p>
      <p class="venue-line"><svg viewBox="0 0 32 32" style="--icon-stroke: var(--wine-bright)"><circle cx="16" cy="16" r="16" fill="var(--wine-bright)"/><use href="#icon-mail" style="color:#fff"/></svg>info@pcta.pt</p>
    </div>
  </article>
</section>

</body>
</html>
```